Western Canadian Survey Company needs Business Card and Letter Head Design

Hello,

We're looking to have our business cards redesigned along with our letterhead.

We've recently changed out logo and would like to use this. Please use some creativity and propose different options (Traditional and modern).

We will provide as much feedback as possible.

Business card should be double sided with our logo. We would also like room for cell phone number, email address and position. Back of the card can just be our logo or potentially a list of our services we provide.

Industry/Entity Type

Business

Contact Information for Business Card

```html
<!DOCTYPE html>
<html lang="en">
<head>
<meta charset="utf-8">
<title>Linemark Field Surveys Ltd – Stationery</title>
<link rel="stylesheet" href="https://fonts.googleapis.com/css2?family=Open+Sans:wght@400;600;700&display=swap">
<style>
  :root {
    --ink: #1f2225;
    --black: #121314;
    --steel: #4d6a81;
    --steel-dark: #3c5567;
    --paper: #ffffff;
    --backdrop: #e4e5e6;
    --muted: #6b7075;
    --rule: #2a2d30;
  }
  * { box-sizing: border-box; margin: 0; padding: 0; }
  html, body { width: 1200px; height: 2571px; overflow: hidden; }
  body {
    position: relative;
    background: var(--backdrop);
    font-family: "Open Sans", Arial, sans-serif;
    color: var(--ink);
  }
  .sheet { position: absolute; background: var(--paper); overflow: hidden; box-shadow: 0 2px 10px rgba(0,0,0,.12); }

  /* brand lockup */
  .brand { position: absolute; display: flex; align-items: center; gap: 8px; }
  .brand-square { width: 12px; height: 12px; background: var(--steel); flex: none; }
  .brand-name { font-weight: 700; color: var(--steel); letter-spacing: .04em; white-space: nowrap; }
  .brand-rule { position: absolute; height: 2px; background: var(--rule); }

  /* business card front */
  .card { width: 540px; height: 309px; top: 120px; }
  .card-front { left: 40px; }
  .card-front .brand { left: 22px; top: 132px; gap: 7px; }
  .card-front .brand-square { width: 10px; height: 10px; }
  .card-front .brand-name { font-size: 12px; letter-spacing: .02em; }
  .card-front .brand-rule { left: 22px; top: 156px; width: 232px; }
  .person { position: absolute; left: 300px; top: 62px; right: 0; }
  .person-name { font-size: 22px; font-weight: 700; color: var(--ink); line-height: 1.1; }
  .person-title { font-size: 14px; color: var(--steel); line-height: 1.3; }
  .person-bar { height: 6px; background: var(--steel); margin-left: 64px; margin-top: -4px; }
  .contact-list { position: absolute; left: 290px; top: 140px; list-style: none; }
  .contact-list li { display: flex; align-items: flex-start; gap: 12px; font-size: 12px; line-height: 1.35; margin-bottom: 8px; color: var(--ink); }
  .contact-list svg { width: 13px; height: 13px; flex: none; margin-top: 1px; fill: var(--steel); }
  .services-band {
    position: absolute; left: 0; right: 0; bottom: 0;
    background: var(--steel); color: #e9eef2;
    font-size: 10px; font-style: italic; white-space: nowrap;
    display: flex; align-items: center;
  }
  .card-front .services-band { height: 28px; padding-left: 18px; border-top: 3px solid var(--rule); }

  /* business card back */
  .card-back { left: 620px; background: var(--black); }
  .card-back .brand { left: 50%; top: 132px; transform: translateX(-50%); }
  .card-back .brand-name { font-size: 17px; color: var(--steel); }
  .card-back .brand-rule { left: 135px; width: 270px; top: 166px; background: var(--steel); height: 1px; }

  /* letterhead */
  .letterhead { left: 40px; top: 549px; width: 720px; height: 1018px; }
  .letterhead .brand { left: 48px; top: 46px; }
  .letterhead .brand-name { font-size: 14px; }
  .letterhead .brand-rule { left: 48px; top: 72px; width: 230px; }
  .letterhead .person { left: 470px; top: 92px; }
  .letterhead .person-name { font-size: 17px; }
  .letterhead .person-title { font-size: 12px; }
  .letterhead .person-bar { height: 4px; margin-left: 52px; margin-top: -3px; }
  .letter-body { position: absolute; left: 60px; right: 60px; top: 170px; font-size: 13px; line-height: 1.95; color: #3b3f43; }
  .letter-body p { margin-bottom: 18px; text-align: justify; }
  .letter-sign { margin-top: 26px; }
  .letter-sign strong { display: block; color: var(--ink); }
  .footer-contact {
    position: absolute; left: 0; right: 0;
    display: flex; justify-content: space-between; align-items: center;
    font-size: 10px; color: var(--ink); border-top: 3px solid var(--steel);
  }
  .footer-contact span { display: flex; align-items: center; gap: 5px; white-space: nowrap; }
  .footer-contact svg { width: 10px; height: 10px; fill: var(--steel); }
  .letterhead .footer-contact { bottom: 30px; height: 30px; padding: 0 40px; }
  .letterhead .services-band { height: 30px; justify-content: center; }

  /* folder */
  .folder { left: 800px; top: 549px; width: 360px; height: 509px; background: var(--black); }
  .folder .brand { left: 50%; top: 226px; transform: translateX(-50%); }
  .folder .brand-name { font-size: 15px; color: var(--steel); }
  .folder .brand-rule { left: 60px; width: 240px; top: 256px; background: var(--steel); height: 1px; }

  /* envelope back */
  .envelope-back { left: 800px; top: 1118px; width: 360px; height: 180px; }
  .envelope-flap { position: absolute; inset: 0; width: 100%; height: 100%; }
  .envelope-back .brand { left: 50%; top: 30px; transform: translateX(-50%); }
  .envelope-back .brand-name { font-size: 10px; color: var(--steel); }

  /* envelope front */
  .envelope-front { left: 40px; top: 1687px; width: 1120px; height: 560px; }
  .envelope-front .brand { left: 60px; top: 56px; }
  .envelope-front .brand-name { font-size: 18px; }
  .envelope-front .brand-rule { left: 60px; top: 90px; width: 300px; }
  .envelope-front .footer-contact { bottom: 46px; height: 42px; padding: 0 60px; font-size: 13px; }
  .envelope-front .footer-contact svg { width: 13px; height: 13px; }
  .envelope-front .services-band { height: 46px; justify-content: center; font-size: 14px; }
</style>
</head>
<body>

<svg width="0" height="0" style="position:absolute" aria-hidden="true">
  <defs>
    <symbol id="icon-pin" viewBox="0 0 24 24"><path d="M12 2a7 7 0 0 0-7 7c0 5.2 7 13 7 13s7-7.8 7-13a7 7 0 0 0-7-7zm0 9.5A2.5 2.5 0 1 1 12 6.5a2.5 2.5 0 0 1 0 5z"/></symbol>
    <symbol id="icon-phone" viewBox="0 0 24 24"><path d="M6.6 10.8a15.1 15.1 0 0 0 6.6 6.6l2.2-2.2c.3-.3.7-.4 1-.2 1.1.4 2.3.6 3.6.6.6 0 1 .4 1 1V20c0 .6-.4 1-1 1A17 17 0 0 1 3 4c0-.6.4-1 1-1h3.5c.6 0 1 .4 1 1 0 1.3.2 2.5.6 3.6.1.3 0 .7-.2 1z"/></symbol>
    <symbol id="icon-mail" viewBox="0 0 24 24"><path d="M2 5h20v14H2zm2 2v.5l8 5 8-5V7zm0 3v7h16v-7l-8 5z"/></symbol>
    <symbol id="icon-web" viewBox="0 0 24 24"><path d="M12 2a10 10 0 1 0 0 20 10 10 0 0 0 0-20zm6.9 6h-3a15.7 15.7 0 0 0-1.3-4A8 8 0 0 1 18.9 8zM12 4c.8 1.2 1.5 2.5 1.9 4h-3.8c.4-1.5 1.1-2.8 1.9-4zM4.3 14a8 8 0 0 1 0-4h3.4a16 16 0 0 0 0 4zm.8 2h3a15.7 15.7 0 0 0 1.3 4A8 8 0 0 1 5.1 16zm3-8h-3a8 8 0 0 1 4.3-4c-.6 1.2-1 2.6-1.3 4zM12 20c-.8-1.2-1.5-2.5-1.900-4h3.8c-.4 1.5-1.1 2.8-1.9 4zm2.3-6H9.7a14 14 0 0 1 0-4h4.6a14 14 0 0 1 0 4zm.3 6c.6-1.2 1-2.6 1.3-4h3a8 8 0 0 1-4.3 4zm1.7-6a16 16 0 0 0 0-4h3.4a8 8 0 0 1 0 4z"/></symbol>
  </defs>
</svg>

<section class="sheet card card-front" aria-label="Business card front">
  <div class="brand"><span class="brand-square"></span><span class="brand-name">LINEMARK FIELD SURVEYS LTD</span></div>
  <div class="brand-rule"></div>
  <div class="person">
    <div class="person-name">Daniel Reeves</div>
    <div class="person-title">Manager</div>
    <div class="person-bar"></div>
  </div>
  <ul class="contact-list">
    <li><svg><use href="#icon-pin"/></svg><span>418 Ridgeline Way<br>Vernon, BC. V1T 4K6</span></li>
    <li><svg><use href="#icon-phone"/></svg><span>+780 555 0142</span></li>
    <li><svg><use href="#icon-mail"/></svg><span>hr@linemarksurveys.net</span></li>
    <li><svg><use href="#icon-web"/></svg><span>www.linemarksurveys.ca</span></li>
  </ul>
  <div class="services-band">QA/QC &amp; Survey Control | Construction Surveys | Underground Utility Location | GIS / Drafting</div>
</section>

<section class="sheet card card-back" aria-label="Business card back">
  <div class="brand"><span class="brand-name">LINEMARK FIELD SURVEYS LTD</span></div>
  <div class="brand-rule"></div>
</section>

<section class="sheet letterhead" aria-label="Letterhead">
  <div class="brand"><span class="brand-square"></span><span class="brand-name">LINEMARK FIELD SURVEYS LTD</span></div>
  <div class="brand-rule"></div>
  <div class="person">
    <div class="person-name">Daniel Reeves</div>
    <div class="person-title">Manager</div>
    <div class="person-bar"></div>
  </div>
  <div class="letter-body">
    <p>Dear Client, thank you for choosing our team for your upcoming site work. We have reviewed the drawings and prepared a schedule for control, layout and as-built surveys across each phase of the project.</p>
    <p>Our crews will establish benchmarks before excavation begins, then locate buried utilities and confirm grades as work proceeds. Field data is checked daily and delivered as clean drawings in your preferred format.</p>
    <p>Every measurement is tied to provincial control and reviewed by a licensed surveyor before release, so your contractors can build with confidence from the first stake to final inspection.</p>
    <p>Please review the attached proposal and let us know of any changes to access, timing or scope. We look forward to working with you.</p>
    <div class="letter-sign">Sincerely,<strong>Daniel Reeves</strong></div>
  </div>
  <div class="footer-contact">
    <span><svg><use href="#icon-pin"/></svg>418 Ridgeline Way, Vernon, BC. V1T 4K6</span>
    <span><svg><use href="#icon-phone"/></svg>+780 555 0142</span>
    <span><svg><use href="#icon-mail"/></svg>hr@linemarksurveys.net</span>
    <span><svg><use href="#icon-web"/></svg>www.linemarksurveys.ca</span>
  </div>
  <div class="services-band">QA/QC &amp; Survey Control | Construction Surveys | Underground Utility Location | GIS / Drafting</div>
</section>

<section class="sheet folder" aria-label="Presentation folder cover">
  <div class="brand"><span class="brand-name">LINEMARK FIELD SURVEYS LTD</span></div>
  <div class="brand-rule"></div>
</section>

<section class="sheet envelope-back" aria-label="Envelope back">
  <svg class="envelope-flap" viewBox="0 0 360 180" preserveAspectRatio="none">
    <polygon points="0,0 360,0 360,20 180,110 0,20" fill="var(--black)"/>
    <polyline points="0,180 180,100 360,180" fill="none" stroke="#d8dadc" stroke-width="1"/>
  </svg>
  <div class="brand"><span class="brand-name">LINEMARK FIELD SURVEYS LTD</span></div>
</section>

<section class="sheet envelope-front" aria-label="Envelope front">
  <div class="brand"><span class="brand-square"></span><span class="brand-name">LINEMARK FIELD SURVEYS LTD</span></div>
  <div class="brand-rule"></div>
  <div class="footer-contact">
    <span><svg><use href="#icon-pin"/></svg>418 Ridgeline Way, Vernon, BC. V1T 4K6</span>
    <span><svg><use href="#icon-phone"/></svg>+780 555 0142</span>
    <span><svg><use href="#icon-mail"/></svg>hr@linemarksurveys.net</span>
    <span><svg><use href="#icon-web"/></svg>www.linemarksurveys.ca</span>
  </div>
  <div class="services-band">QA/QC &amp; Survey Control | Construction Surveys | Underground Utility Location | GIS / Drafting</div>
</section>

</body>
</html>
```